Dry ice blasting service provider needs a brochure to give to potential clients

our company TerraBrite provides a dry ice blasting service, it is a surface cleaning and preparation system.

I would like a couple before and after pictures included and make sure we emphasise the fact of its ; environmentally preferred. no chemicals used and no secondary waste is produced.

I will now add in its application/benefits and a quick run down on how it actually works. Obviously you don't have to put all info in as it wouldn't fit on A4 but better u have more info than not enough.

Applications : Oil&Gas, Offshore, Power Generation, Asphalt equipment , Mining , Fire and restoration, Industrial Electrics , Transport, Pulp and Paper industry , Pharmaceuticals, Marine , Aircraft, Food processing ,Foundries .

Benefits :There are numerous benefits to be gained by contracting TerraBrite. Primary benefits are outlined below. Solely they have the potential to impact your business operations but we combine them for a cleaner , greener maintenance solution.

COST SAVINGS: TerraBrite is committed to keeping costs down without it costing the environment.

HOW ?

+Minimal downtime - In situ and online cleaning
+No secondary waste - Dry ice sublimates back to a gas (no residue)
+Moisture Free - Non conductive, Electrical Friendly
+No chemicals - Toxic chemicals are not needed to clean equipment

WHAT?

Dry ice blasting is the modern alternative to chemical cleaning, sandblasting, water blasting, steam cleaning, manual scrubbing, scraping, and hand tooling, and is the most effective and efficient method of cleaning available today. Dry ice cleaning uses soft dry ice, accelerated at supersonic speeds, and creates mini-explosions on the surface to lift the undesirable item off the underlying substrate. Thermal shock also breaks the bond between the Base material and contaminant.

Guaranteed. Please put in abit more effort into the wording as i see you have simply cut and paste. Some of the wording must go in certain sequence... Please add contact details on it somewhere. - PO box 387 Karvale 6921 Western Australia Australia TerraBrite@mailbarn.example Australia - +61 408 163 742 Indonesia - +62 0857 4126 7180 Servicing Asia Pacific Based in Perth and Indonesia

Target Market(s)

Men in there mid 40's + in management roles who want a precise job done quickly and efficiently.

Industry/Entity Type

Industry

Colors
acd037
33a6d7

Requirements
Must have
• Contact details
"Cleaner , Greener solutions for the Asia Pacific market"

```html
<!DOCTYPE html>
<html lang="en">
<head>
<meta charset="utf-8">
<title>TerraBrite – Dry Ice Blasting</title>
<link href="https://fonts.googleapis.com/css2?family=Didact+Gothic&family=Open+Sans:ital,wght@0,400;1,700&display=swap" rel="stylesheet">
<style>
  :root {
    --green: #acd037;
    --blue: #33a6d7;
    --text: #6d6d6d;
    --paper: #ffffff;
    --white: #ffffff;
  }
  * { margin: 0; padding: 0; box-sizing: border-box; }
  html, body { width: 1200px; height: 849px; overflow: hidden; background: var(--paper); }
  .brochure {
    position: relative; width: 1200px; height: 849px; overflow: hidden;
    background: radial-gradient(ellipse at 50% 45%, #ffffff 40%, #f1f1f1 100%);
    font-family: "Didact Gothic", "Century Gothic", sans-serif; color: var(--text);
  }
  .top-band { position: absolute; left: 0; top: 0; width: 1200px; height: 33px; background: var(--green); }
  .bottom-band {
    position: absolute; left: 0; top: 814px; width: 1200px; height: 35px; background: var(--blue);
    font-family: "Open Sans", Arial, sans-serif; color: var(--white); font-size: 15.5px; letter-spacing: 0.6px;
  }
  .bottom-band .phone { position: absolute; top: 7px; }
  .phone-au { left: 331px; }
  .phone-id { right: 43px; }

  .bar { position: absolute; height: 17px; background: var(--blue); clip-path: polygon(6px 0, 100% 0, calc(100% - 6px) 100%, 0 100%); }
  .heading {
    position: absolute; font-family: "Open Sans", Arial, sans-serif; font-style: italic; font-weight: 700;
    color: var(--green); font-size: 22px; letter-spacing: 0.3px; line-height: 1;
  }
  .subheading { font-size: 17px; }
  .copy { position: absolute; font-size: 12.6px; line-height: 16.5px; }
  .what-copy { left: 323px; top: 227px; width: 225px; text-align: justify; line-height: 20.2px; }

  .photo { position: absolute; }
  .photo-engine-before { left: 45px; top: 192px; width: 264px; height: 190px; background: linear-gradient(150deg, #8a8f8a, #4e534f 55%, #2e3230); }
  .photo-engine-after { left: 45px; top: 405px; width: 262px; height: 200px; background: linear-gradient(150deg, #c9cbc6, #5b6660 50%, #3c4640); }
  .photo-coil-before { left: 641px; top: 98px; width: 275px; height: 406px; background: linear-gradient(160deg, #9c8a70, #6f5a45 50%, #4a3a2d); }
  .photo-coil-after { left: 918px; top: 98px; width: 234px; height: 406px; background: linear-gradient(160deg, #b35a5e, #8a2d36 50%, #5e1d26); }

  .applications { left: 641px; top: 522px; width: 511px; }
  .applications strong { color: var(--blue); font-weight: 400; }
  .how-list { list-style: none; left: 653px; top: 664px; width: 540px; }

  .tagline {
    position: absolute; left: 45px; top: 752px;
    font-family: "Open Sans", Arial, sans-serif; font-style: italic; font-weight: 700;
    color: var(--blue); font-size: 17px; letter-spacing: 0.3px;
  }
  .contact { left: 653px; top: 745px; width: 520px; }
</style>
</head>
<body>
<main class="brochure">
  <div class="top-band"></div>

  <div class="bar" style="left:-6px; top:99px; width:44px;"></div>
  <h2 class="heading" style="left:45px; top:95px;">COST SAVINGS:</h2>
  <div class="bar" style="left:220px; top:99px; width:380px;"></div>
  <p class="copy" style="left:45px; top:134px;">TerraBrite keeps your maintenance costs down, without passing the cost on to the environment.</p>

  <div class="photo photo-engine-before" role="img" aria-label="Before: dirty engine inside machinery housing"></div>
  <div class="photo photo-engine-after" role="img" aria-label="After: engine cleaned with dry ice blasting"></div>

  <h3 class="heading subheading" style="left:323px; top:192px;">WHAT?</h3>
  <p class="copy what-copy">Dry ice blasting is the modern replace&shy;ment for chemical cleaning, sandblasting, water blasting, steam cleaning, manual scrubbing, scraping and hand tooling, and the most effective and efficient cleaning method available today. Soft dry ice pellets are accelerated to supersonic speeds, creating tiny explosions on impact that lift contaminants away from the underlying surface. At the same time, thermal shock breaks the bond between the base material and the contaminant.</p>

  <div class="photo photo-coil-before" role="img" aria-label="Before: contaminated generator stator windings"></div>
  <div class="photo photo-coil-after" role="img" aria-label="After: cleaned generator stator windings"></div>

  <p class="copy applications"><strong>Applications:</strong> Oil &amp; Gas · Offshore · Power Generation · Asphalt Equipment · Mining · Fire &amp; Restoration · Industrial Electrics · Transport · Pulp &amp; Paper · Pharmaceuticals · Marine · Aircraft · Food Processing · Foundries</p>

  <div class="bar" style="left:-6px; top:625px; width:44px;"></div>
  <h2 class="heading" style="left:45px; top:621px;">BENEFITS:</h2>
  <div class="bar" style="left:179px; top:625px; width:478px;"></div>
  <p class="copy" style="left:45px; top:662px; width:500px;">Contracting TerraBrite brings a range of benefits to your operation, and the key ones are outlined here. Each can improve your business on its own; combined, they deliver a cleaner, greener maintenance solution.</p>

  <p class="tagline">Cleaner, Greener solutions for the Asia Pacific market</p>

  <h2 class="heading" style="left:665px; top:623px;">HOW ?</h2>
  <div class="bar" style="left:766px; top:627px; width:440px;"></div>
  <ul class="copy how-list">
    <li>+Minimal downtime - Cleaning in situ, often while equipment stays online</li>
    <li>+No secondary waste - Dry ice sublimates back to a gas, leaving no residue</li>
    <li>+Moisture free - Non-conductive and safe around electrics</li>
    <li>+No chemicals - No toxic chemicals are needed to clean equipment</li>
  </ul>

  <p class="copy contact">PO box 387 Karvale 6921 Western Australia · TerraBrite@mailbarn.example<br>Based in Perth and Indonesia · Servicing Asia Pacific</p>

  <footer class="bottom-band">
    <span class="phone phone-au">Australia - +61 408 163 742</span>
    <span class="phone phone-id">Indonesia - +62 0857 4126 7180</span>
  </footer>
</main>
</body>
</html>
```